Business card with professional look

I would like a creative yet professional looking business card for our business. We sell broadcast TV related security products for mobile phones, set top boxes, and tablets. Our customers are international. We have a logo we like and I would like to possibly add some color to the business card but keep it professional looking.

Target Market(s)

Professionals in the TV, cable, ans Satellite industries

Industry/Entity Type

Cable Tv

Contact Information for Business Card

Name Ned Vastermill, title CEO, Address 8130 Harborline Court, Suite 400, Del Arvo, CA 91584 USA, phone numbers m:+1.619.284.7302 o:+1.855.672.9140, email, logo

Font styles to use
Other font styles liked:
• Open to any font that looks good with logo

Requirements
Must have
• professional look with colors coordinated with logo colors. would like to add one or two different colors as well as some form of background color

```html
<!DOCTYPE html>
<html lang="en">
<head>
<meta charset="utf-8">
<title>Vantelle Business Card</title>
<link rel="stylesheet" href="https://fonts.googleapis.com/css2?family=Montserrat:wght@400;500;600&display=swap">
<style>
  :root {
    --bg: #e9e6e1;
    --card: #0b0b0c;
    --card-sheen: #1d1e21;
    --blue: #2a63c4;
    --blue-light: #4f8fdc;
    --text: #f2f2f2;
    --muted: #8a8d93;
  }
  html, body {
    margin: 0;
    width: 1200px;
    height: 1022px;
    overflow: hidden;
    background: var(--bg);
    font-family: "Montserrat", sans-serif;
  }
  .card {
    position: absolute;
    left: 150px;
    top: 254px;
    width: 900px;
    height: 514px;
    border-radius: 18px;
    background: linear-gradient(135deg, var(--card) 0%, var(--card-sheen) 45%, var(--card) 75%);
    box-shadow: 0 18px 40px rgba(0,0,0,0.25);
    overflow: hidden;
  }
  .card__edge {
    position: absolute;
    right: 0;
    top: 0;
    width: 10px;
    height: 100%;
    background: var(--blue);
  }
  .brand {
    position: absolute;
    left: 90px;
    top: 150px;
    display: flex;
    align-items: center;
    gap: 18px;
    font-weight: 600;
    font-size: 62px;
    color: var(--muted);
    letter-spacing: -1px;
  }
  .brand__mark {
    width: 54px;
    height: 54px;
    background: var(--blue-light);
  }
  .divider {
    position: absolute;
    left: 70px;
    right: 110px;
    top: 345px;
    height: 3px;
    background: var(--blue);
  }
  .person {
    position: absolute;
    right: 110px;
    top: 262px;
    text-align: right;
  }
  .person__name {
    font-weight: 600;
    font-size: 34px;
    color: var(--blue);
    letter-spacing: 0.5px;
  }
  .person__title {
    font-size: 22px;
    color: var(--text);
    margin-top: 4px;
  }
  .address {
    position: absolute;
    right: 110px;
    top: 366px;
    text-align: right;
    font-size: 21px;
    line-height: 1.45;
    color: var(--text);
  }
  .contact {
    position: absolute;
    left: 90px;
    top: 366px;
    list-style: none;
    margin: 0;
    padding: 0;
    font-size: 21px;
    line-height: 1.45;
    color: var(--text);
  }
  .contact li {
    display: flex;
    align-items: center;
    gap: 12px;
  }
  .contact svg {
    width: 16px;
    height: 16px;
    stroke: var(--blue-light);
    fill: none;
    stroke-width: 1.8;
  }
  .contact strong { font-weight: 600; }
</style>
</head>
<body>
  <div class="card">
    <div class="card__edge"></div>

    <div class="brand">
      <span>Vantelle</span>
      <span class="brand__mark"></span>
    </div>

    <div class="person">
      <div class="person__name">Ned Vastermill</div>
      <div class="person__title">CEO</div>
    </div>

    <div class="divider"></div>

    <ul class="contact">
      <li>
        <svg viewBox="0 0 16 16"><rect x="4" y="1.5" width="8" height="13" rx="1.5"/><line x1="7" y1="12" x2="9" y2="12"/></svg>
        +1.619.284.7302
      </li>
      <li>
        <svg viewBox="0 0 16 16"><path d="M4 2 L6.5 2 L7.5 5 L6 6.5 C7 8.5 7.5 9 9.5 10 L11 8.5 L14 9.5 L14 12 C14 13 13 14 12 14 C7 14 2 9 2 4 C2 3 3 2 4 2 Z"/></svg>
        +1.855.672.9140
      </li>
      <li>
        <svg viewBox="0 0 16 16"><rect x="1.5" y="3" width="13" height="10" rx="1"/><polyline points="1.5,3.5 8,9 14.5,3.5"/></svg>
        <span>info@<strong>vantelle</strong>.com</span>
      </li>
    </ul>

    <div class="address">
      8130 Harborline Court,<br>
      Suite 400, Del Arvo,<br>
      CA 91584 USA
    </div>
  </div>
</body>
</html>
```